Telecommunications/Power civil contractor needs business card design

Were a new telecommunications/power underground civil contractor that is looking for a new business card design. Our company colours are silver or grey and orange. Feel free to use the white background logo or the black background logo.

Target Market(s)

Local contractors, utility companies, private sector mining/energy companies, developers.

Industry/Entity Type

Telecommunications

Contact Information for Business Card

Each card will need the following info:
Persons name:
Title:
E-mail:
Phone number:
Shop Address:
Mailing Address:

Requirements
Must have
• Each card will need the following info:
• Persons name:
• Title:
• E-mail:
• Phone number:
• Shop Address:
• Mailing Address:

```html
<!DOCTYPE html>
<html lang="en">
<head>
<meta charset="utf-8">
<title>Ridgeline Civil Works Inc – Business Card</title>
<link href="https://fonts.googleapis.com/css2?family=Arimo:wght@400;700&display=swap" rel="stylesheet">
<style>
  :root {
    --backdrop: #1c1c1c;
    --orange: #f05a28;
    --panel-grey: #6a6a6a;
    --paper-light: #f4f4f4;
    --paper-shade: #d9d9d9;
    --ink-grey: #5a5a5a;
    --white: #ffffff;
  }
  * { box-sizing: border-box; margin: 0; padding: 0; }
  html, body {
    width: 1200px; height: 800px; overflow: hidden;
    background: var(--backdrop);
    font-family: "Arimo", Arial, sans-serif;
  }
  .sheet {
    width: 1200px; height: 800px;
    display: flex; align-items: center; justify-content: center; gap: 50px;
  }
  .card {
    width: 540px; height: 309px;
    position: relative; overflow: hidden;
    box-shadow: 0 10px 30px rgba(0,0,0,.5);
  }

  /* Front face */
  .card--front { display: flex; }
  .brand-side {
    width: 55%;
    background: linear-gradient(135deg, var(--white) 0%, var(--paper-light) 50%, var(--paper-shade) 100%);
    display: flex; flex-direction: column; align-items: center; justify-content: center; gap: 14px;
  }
  .brand-mark {
    width: 56px; height: 56px; border-radius: 50%;
    border: 4px solid var(--orange);
  }
  .brand-name {
    font-weight: 700; font-size: 22px; color: var(--ink-grey);
    text-align: center; line-height: 1.15; letter-spacing: .5px;
    text-transform: uppercase;
  }
  .contact-side {
    width: 45%;
    background: var(--panel-grey);
    color: var(--white);
    padding: 40px 12px 0 28px;
    font-size: 13px;
    white-space: nowrap;
  }
  .person-name { font-weight: 700; font-size: 17px; }
  .person-title { font-size: 12px; margin-top: 2px; }
  .contact-lines { margin-top: 34px; line-height: 1.45; font-size: 12.5px; }
  .address-lines { margin-top: 28px; line-height: 2.1; }

  /* Back face */
  .card--back {
    background: var(--orange);
    display: flex; flex-direction: column; align-items: center; justify-content: center; gap: 18px;
  }
  .back-mark {
    width: 110px; height: 110px; border-radius: 50%;
    border: 7px solid var(--white);
  }
  .back-name {
    color: var(--white); font-weight: 700; font-size: 24px;
    letter-spacing: .5px; text-transform: uppercase;
  }
</style>
</head>
<body>
<main class="sheet">
  <section class="card card--front">
    <div class="brand-side">
      <div class="brand-mark"></div>
      <div class="brand-name">Ridgeline<br>Civil Works Inc</div>
    </div>
    <div class="contact-side">
      <p class="person-name">Persons Name</p>
      <p class="person-title">Title</p>
      <div class="contact-lines">
        <p>p: 555 014 2288</p>
        <p>e: personsname@example.com</p>
      </div>
      <div class="address-lines">
        <p>Shop Address:</p>
        <p>Mailing Address:</p>
      </div>
    </div>
  </section>
  <section class="card card--back">
    <div class="back-mark"></div>
    <div class="back-name">Ridgeline Civil Works Inc</div>
  </section>
</main>
</body>
</html>
```